New Website for consulting company

We need a completely new design for our company web site: www.morvane-partners.ch (please do not use it as a reference. We want something completely different.)
We are a consulting company and therefore our team is our key ressource together with our skills.
This site will be german in the first place. It will be the webmasters job to create it multilingual.
The website should be rather eccentric but still informative.
For colors and logo please refer to attached Logodefinition.pdf. The colored horizontal logo should be somehow used for the website but doesn't need to be extremely prominent. You can choose every color for the design but the logo must be somehow embedded in original colors and the green should be integrated for the site.
Please keep in mind that it should also work for mobile devices so the webmaster will have to create a responsive website out of the submitted design.
The main Page should be a one pager with different layout blocks directly accessible via top sticky menubar.:
- AKTEURE (team), gallery, people centric with images of member and expandable description box, plus skills abstract list (name & description). See attached mockups to support the explaining (do not take it as a reference).
- ÜBER UNS (mission), Description of companies vision, mission, competences etc.
- ... according to the menu bar
We would like to have at least 3 different block layouts to fill with content for the one pager site:
1. Team is the most important and the least generic one
2. Big picture less text
3. Multiple smaller pictures multiple text blocks
4. Hardly any picture text centric
The page should communicate competence in what we are doing, quality and not least youth and freshness.
See Attachements:
- Logodefinition.pdf: Logo definition containing definition of color of the logo.
- mockup_Website_mock1.png: These should give you an impression of how it is meant to have layouted blocks

```html
<!DOCTYPE html>
<html lang="de">
<head>
<meta charset="utf-8">
<title>Morvane Partners – Consulting</title>
<link href="https://fonts.googleapis.com/css2?family=Dosis:wght@400;500;600;700&family=Open+Sans:wght@400;600&display=swap" rel="stylesheet">
<style>
:root{
  --green:#6cbf3b;
  --green-dark:#58a82c;
  --ink:#222;
  --text:#555;
  --muted:#888;
  --card:#232325;
  --dark:#2a2a2c;
  --line:#e4e4e4;
  --white:#fff;
}
*{margin:0;padding:0;box-sizing:border-box}
html,body{width:1200px;height:2517px;overflow:hidden;background:var(--white)}
body{font-family:'Open Sans',sans-serif;color:var(--text);position:relative}

/* header + hero */
.hero{position:absolute;left:0;top:0;width:1200px;height:590px;
  background:linear-gradient(100deg,#cfcac0 0%,#8c8577 28%,#4a453e 55%,#2f2c28 78%,#5b5348 100%)}
.topbar{position:absolute;left:0;top:0;width:1200px;height:62px;background:rgba(20,20,20,.82)}
.brand{position:absolute;left:84px;top:0;width:131px;height:98px;background:var(--green);
  display:flex;flex-direction:column;align-items:center;justify-content:center;
  font-family:'Dosis',sans-serif;font-weight:700;color:var(--white);line-height:1}
.brand .b1{font-size:32px}
.brand .b2{font-size:17px;margin-top:4px}
.nav{position:absolute;left:310px;top:17px;display:flex;gap:4px;align-items:center;
  font-family:'Dosis',sans-serif;font-weight:600;font-size:14px;color:var(--white);white-space:nowrap}
.nav a{color:inherit;text-decoration:none;padding:4px 11px;border-radius:15px;border:2px solid transparent}
.nav a.active{border-color:var(--white)}
.social{position:absolute;left:952px;top:18px;display:flex;gap:9px}
.social span{width:26px;height:26px;border-radius:50%;background:var(--white)}
.social span.on{background:var(--green)}

/* team */
.section-title{font-family:'Dosis',sans-serif;font-weight:600;color:var(--green);font-size:32px;text-align:center}
.team-title{position:absolute;top:644px;left:0;width:1200px}
.team-grid{position:absolute;left:84px;top:716px;width:1032px;display:grid;
  grid-template-columns:repeat(6,160px);column-gap:14.4px;row-gap:16px}
.member{height:255px;background:var(--card);display:flex;flex-direction:column}
.member .photo{height:175px;background:linear-gradient(160deg,#8aa05e,#5d6f3c 55%,#3e4a2a)}
.member .photo.alt{background:linear-gradient(160deg,#a4a18a,#6d6a55 55%,#3a3a30)}
.member .name{font-size:13px;font-weight:600;color:var(--white);text-align:center;margin-top:14px}
.member .rule{width:110px;height:2px;background:#555;margin:9px auto 0}
.member .role{font-size:12px;color:var(--white);text-align:center;margin-top:10px}

/* mission */
.mission{position:absolute;left:0;top:1315px;width:1200px;height:467px;
  background:linear-gradient(120deg,#3a3a3c,#232325 50%,#323234)}
.mission h2{font-family:'Dosis',sans-serif;font-weight:700;color:var(--white);font-size:34px;text-align:center;margin-top:58px}
.mission .underline{width:62px;height:3px;background:var(--green);margin:12px auto 0}
.mission p{width:960px;margin:26px auto 0;text-align:center;color:#e8e8e8;font-size:14px;line-height:1.75}
.mission p+p{margin-top:22px}
.btn{display:block;width:180px;height:46px;margin:44px auto 0;border-radius:23px;background:var(--green);
  color:var(--white);font-family:'Dosis',sans-serif;font-weight:600;font-size:17px;text-align:center;line-height:46px;text-decoration:none}

/* competencies */
.comp-title{position:absolute;left:84px;top:1815px;font-family:'Dosis',sans-serif;font-weight:700;font-size:26px;color:var(--ink)}
.comp-image{position:absolute;left:84px;top:1868px;width:453px;height:235px;
  background:linear-gradient(135deg,#e6e9ec,#8f969d 45%,#2e3438)}
.comp-text{position:absolute;left:557px;top:1860px;width:260px;font-size:13px;line-height:1.65;color:var(--muted)}
.comp-text p+p{margin-top:18px}
.comp-list{position:absolute;left:890px;top:1866px;width:224px;list-style:none}
.comp-list li{font-size:13px;color:var(--text);height:39px;line-height:39px;border-bottom:1px solid var(--line);padding-left:16px;position:relative}
.comp-list li::before{content:"›";position:absolute;left:0;color:var(--green);font-weight:600}
.comp-list li.current{color:var(--green)}
.divider{position:absolute;left:84px;top:2173px;width:1032px;height:1px;background:var(--line)}

/* contact */
.contact-title{position:absolute;left:84px;top:2232px;font-family:'Dosis',sans-serif;font-weight:700;font-size:22px;color:var(--ink)}
.contact-lead{position:absolute;left:84px;top:2262px;font-size:13px;color:var(--muted)}
.company{position:absolute;left:84px;top:2284px;font-size:14px;font-weight:600;color:var(--green)}
.contact-col{position:absolute;top:2322px;font-size:12px;line-height:1.6;color:var(--text)}
.partner-img{position:absolute;left:839px;top:2246px;width:133px;height:132px;background:linear-gradient(135deg,#ddd,#9a9a9a)}
.partner-name{position:absolute;left:980px;top:2246px;width:133px;height:132px;background:#9c9c9c;
  display:flex;align-items:center;justify-content:center;text-align:center;
  font-family:'Dosis',sans-serif;font-weight:700;font-size:22px;line-height:1.1;color:var(--white)}

/* footer */
.footer{position:absolute;left:0;top:2453px;width:1200px;height:64px;background:var(--green);
  color:var(--white);font-size:13px;text-align:center;line-height:64px}
</style>
</head>
<body>

<header>
  <div class="hero" role="img" aria-label="Photo of two colleagues working together on a sofa with a laptop and documents in a bright living room"></div>
  <div class="topbar"></div>
  <div class="brand"><span class="b1">Morvane</span><span class="b2">Partners</span></div>
  <nav class="nav">
    <a class="active" href="#">Home</a>
    <a href="#">Competencies</a>
    <a href="#">Team</a>
    <a href="#">Customers</a>
    <a href="#">Network</a>
    <a href="#">Business</a>
    <a href="#">Contact Us</a>
  </nav>
  <div class="social"><span></span><span class="on"></span><span></span><span></span><span></span></div>
</header>

<section>
  <h2 class="section-title team-title">Morvane Partners Team</h2>
  <div class="team-grid">
    <div class="member"><div class="photo" role="img" aria-label="Portrait of team member"></div><div class="name">Lukas Brenner</div><div class="rule"></div><div class="role">Project Manager</div></div>
    <div class="member"><div class="photo alt" role="img" aria-label="Portrait of team member"></div><div class="name">Lukas Brenner</div><div class="rule"></div><div class="role">Project Manager</div></div>
    <div class="member"><div class="photo" role="img" aria-label="Portrait of team member"></div><div class="name">Lukas Brenner</div><div class="rule"></div><div class="role">Project Manager</div></div>
    <div class="member"><div class="photo alt" role="img" aria-label="Portrait of team member"></div><div class="name">Lukas Brenner</div><div class="rule"></div><div class="role">Project Manager</div></div>
    <div class="member"><div class="photo" role="img" aria-label="Portrait of team member"></div><div class="name">Lukas Brenner</div><div class="rule"></div><div class="role">Project Manager</div></div>
    <div class="member"><div class="photo alt" role="img" aria-label="Portrait of team member"></div><div class="name">Lukas Brenner</div><div class="rule"></div><div class="role">Project Manager</div></div>
    <div class="member"><div class="photo" role="img" aria-label="Portrait of team member"></div><div class="name">Lukas Brenner</div><div class="rule"></div><div class="role">Project Manager</div></div>
    <div class="member"><div class="photo alt" role="img" aria-label="Portrait of team member"></div><div class="name">Lukas Brenner</div><div class="rule"></div><div class="role">Project Manager</div></div>
    <div class="member"><div class="photo" role="img" aria-label="Portrait of team member"></div><div class="name">Lukas Brenner</div><div class="rule"></div><div class="role">Project Manager</div></div>
    <div class="member"><div class="photo alt" role="img" aria-label="Portrait of team member"></div><div class="name">Lukas Brenner</div><div class="rule"></div><div class="role">Project Manager</div></div>
    <div class="member"><div class="photo" role="img" aria-label="Portrait of team member"></div><div class="name">Lukas Brenner</div><div class="rule"></div><div class="role">Project Manager</div></div>
    <div class="member"><div class="photo alt" role="img" aria-label="Portrait of team member"></div><div class="name">Lukas Brenner</div><div class="rule"></div><div class="role">Project Manager</div></div>
  </div>
</section>

<section class="mission" role="img" aria-label="Dimmed background photo of a desk with laptop and notes">
  <h2>A collaboration that bears fruit.</h2>
  <div class="underline"></div>
  <p>Die Herausforderungen unserer Kunden sind geprägt durch stetig wachsende Qualitätsansprüche, durch immer schnellere Veränderungszyklen, sei dies aufgrund von Marktgegebenheiten, von gesetzlichen Regulatorien oder von finanziellen Rahmenbedingungen.</p>
  <p>Diese Herausforderungen können meist nicht alleine durch den Einsatz von Informatikmitteln gemeistert werden. Eine rein technische Betrachtung kann sich fatal auf das Business auswirken. Gefragt ist eine ganzheitliche, vernetzte Betrachtung der Problemstellungen und deren Lösungsvarianten unter Berücksichtigung von strategischen, organisatorischen, wirtschaftlichen und technischen Aspekten; nur so lässt sich eine optimale Lösung erreichen.</p>
  <a class="btn" href="#">Read More</a>
</section>

<section>
  <h2 class="comp-title">Competencies</h2>
  <div class="comp-image" role="img" aria-label="Close-up photo of a compass pointing to the word competence"></div>
  <div class="comp-text">
    <p>For us, competence means combined with our experience to use our applied knowledge.</p>
    <p>With our skills for the holistic conception, management and implementation of changes at the interface between business and IT, we support our customers in strategic projects.</p>
    <p>The professional design tasks to strategy, process and system level are needed here as well.</p>
  </div>
  <ul class="comp-list">
    <li class="current">Project Management</li>
    <li>Business Engineering</li>
    <li>ECM / SEVER</li>
    <li>Process Management</li>
    <li>Strategy Consulting</li>
    <li>System Development</li>
  </ul>
  <div class="divider"></div>
</section>

<section>
  <h2 class="contact-title">Contact Info</h2>
  <p class="contact-lead">We are always there for you and look forward to a personal conversation.</p>
  <p class="company">Morvane Partners AG</p>
  <div class="contact-col" style="left:84px">Postfach 418<br>CH-3052 Zollikofen</div>
  <div class="contact-col" style="left:224px">Phone +41 31 555 01 27<br>Web www.morvane-partners.ch<br>email info@morvane-partners.ch</div>
  <div class="contact-col" style="left:462px">VAT No 704.318.552 MWST<br>commercial register CH-035.3.018.214-7<br>bank account IBAN CH44 0000 0000 1234 5678 9</div>
  <div class="partner-img" role="img" aria-label="Grey-toned decorative photo"></div>
  <div class="partner-name">Morvane<br>Partners</div>
</section>

<footer class="footer">Copyright © 2015 Morvane Partners AG | Imprint</footer>

</body>
</html>
```